Emergency Vehicle Installer and Security Firm Needs a Business Card

Our company "Corvalt" need a business card for our Emergency Vehicle Equipment Installation and Infrastructure Security Business. We are contract designers, manufacturers and installers for Emergency Vehicle Fleets. This includes installation of Emergency Lights, Sirens, Vehicle Graphics and Radio Communications. We also supply this products to an international market. We also do consultant, and installation of high level security access, alarm and surveillance equipment for medium to large size businesses.

The design should represent a level of trust in our professionalism and expertise. It should visually display our ongoing relationship with the emergency services, but not overtake our commitment to high level security options.

Target Market(s)

Emergency Services and Businesses requiring high level security

Industry/Entity Type

Business

Contact Information for Business Card

*note complete details will be given to the winning designer for revising. The name "Mark Pell will be used to fill in name".

Mark Pell
Managing Director
Corvalt NZ Limited
Phone: +64 027 604 91352
Email: mark.pell@corvalt-example.co.nz

Requirements
Must have
• Card must be in black. Using our logo on the top as supplied. Designers should try having the reverse side as a blurred image of police lights (red and blue) with our logo in greyscale in the centre (this is not particularly a requirement, but feel free to play around with this option).
Nice to have
• A card design that looks good when spot UV printed. A clean compact and graphic design. A grey scale feel on the front (excluding logo, but you can play around with that idea). Rounded smooth text.
Should not have
• Will update this section as designs come through - feel free to submit what you feel would look good.

```html
<!DOCTYPE html>
<html lang="en">
<head>
<meta charset="utf-8">
<title>Corvalt Business Card</title>
<link rel="stylesheet" href="https://fonts.googleapis.com/css2?family=Open+Sans:wght@400;600;800&display=swap">
<style>
  :root {
    --page-bg: #e9e6e3;
    --card-black: #000000;
    --brand-red: #e8232a;
    --text-white: #ffffff;
    --light-blue: rgba(47,92,255,0.75);
    --light-red: rgba(255,26,26,0.8);
  }
  * { margin: 0; padding: 0; box-sizing: border-box; }
  html, body {
    width: 1200px;
    height: 900px;
    overflow: hidden;
    background: var(--page-bg);
    font-family: "Open Sans", Arial, sans-serif;
  }
  .card {
    position: absolute;
    background: var(--card-black);
    overflow: hidden;
    box-shadow: 0 6px 18px rgba(0,0,0,0.25);
  }

  /* Front */
  .card-front { left: 238px; top: 62px; width: 555px; height: 343px; }
  .holder-name {
    position: absolute; left: 32px; top: 48px;
    color: var(--brand-red); font-size: 20px; font-weight: 600; line-height: 24px;
  }
  .holder-title {
    position: absolute; left: 32px; top: 72px;
    color: var(--text-white); font-size: 16px; font-weight: 400; line-height: 20px;
  }
  .contact-list {
    position: absolute; left: 32px; top: 250px;
    list-style: none; color: var(--text-white); font-size: 16px;
  }
  .contact-list li { display: flex; align-items: center; height: 23px; }
  .contact-list svg { width: 13px; height: 13px; margin-right: 14px; fill: var(--brand-red); }
  .front-brand {
    position: absolute; left: 330px; top: 146px; width: 210px;
    display: flex; align-items: center; gap: 12px;
  }
  .front-brand .brand-dot {
    width: 22px; height: 22px; border-radius: 50%; background: var(--brand-red);
  }
  .front-brand .brand-name {
    color: var(--brand-red); font-size: 34px; font-weight: 800;
  }

  /* Back */
  .card-back { left: 457px; top: 518px; width: 560px; height: 344px; }
  .lights-glow {
    position: absolute; left: 120px; top: 30px; width: 340px; height: 180px;
    background:
      radial-gradient(ellipse 90px 60px at 95px 90px, var(--light-blue), rgba(47,92,255,0) 100%),
      radial-gradient(ellipse 110px 70px at 230px 75px, var(--light-red), rgba(255,26,26,0) 100%);
    filter: blur(6px);
  }
  .back-brand {
    position: absolute; left: 0; right: 0; top: 148px;
    text-align: center;
    color: var(--text-white); font-size: 76px; font-weight: 800; line-height: 1;
  }
  .tagline {
    position: absolute; left: 81px; top: 221px;
    color: var(--text-white); font-size: 16px; font-weight: 400; line-height: 1;
    letter-spacing: 4.5px;
  }
</style>
</head>
<body>
  <section class="card card-front">
    <p class="holder-name">Mark Pell</p>
    <p class="holder-title">Managing Director</p>
    <ul class="contact-list">
      <li>
        <svg viewBox="0 0 24 24" aria-hidden="true"><path d="M6.6 10.8c1.4 2.8 3.8 5.1 6.6 6.6l2.2-2.2c.3-.3.7-.4 1-.2 1.1.4 2.3.6 3.6.6.6 0 1 .4 1 1V20c0 .6-.4 1-1 1C10.6 21 3 13.4 3 4c0-.6.4-1 1-1h3.5c.6 0 1 .4 1 1 0 1.3.2 2.5.6 3.6.1.3 0 .7-.2 1l-2.3 2.2z"/></svg>
        +64 027 604 91352
      </li>
      <li>
        <svg viewBox="0 0 24 24" aria-hidden="true"><path d="M2 5h20v14H2z"/><path d="M3 6l9 7 9-7v1l-9 7-9-7z" fill="#000"/></svg>
        mark.pell@corvalt-example.co.nz
      </li>
    </ul>
    <div class="front-brand">
      <span class="brand-dot"></span>
      <span class="brand-name">Corvalt</span>
    </div>
  </section>

  <section class="card card-back">
    <div class="lights-glow" role="img" aria-label="Blurred red and blue emergency vehicle light bar glowing in the dark"></div>
    <p class="back-brand">CORVALT</p>
    <p class="tagline">ALWAYS ON WATCH</p>
  </section>
</body>
</html>
```